Torvane Systems*

Stationary design including business cards, letter heads, envelops and email signatures using our new logo

Target Market(s)

Innovative Technologies

Industry/Entity Type

Defense Contracting

Font styles to use
Sans Serif

```html
<!DOCTYPE html>
<html lang="en">
<head>
<meta charset="utf-8">
<title>Torvane Systems – Business Card</title>
<link rel="stylesheet" href="https://fonts.googleapis.com/css2?family=Oswald:wght@500;700&family=Arimo:wght@400&display=swap">
<style>
  :root {
    --page-bg: #d9d9d9;
    --card-white: #ffffff;
    --card-black: #0a0a0a;
    --ink: #111111;
    --ink-soft: #333333;
    --rule: #000000;
  }
  * { margin: 0; padding: 0; box-sizing: border-box; }
  html, body {
    width: 1200px; height: 960px; overflow: hidden;
    background: var(--page-bg);
  }
  .canvas {
    position: relative; width: 1200px; height: 960px;
    display: flex; flex-direction: column; align-items: center; justify-content: center; gap: 48px;
  }
  .card {
    position: relative; width: 740px; height: 422px;
    border-radius: 26px; overflow: hidden;
    box-shadow: 0 10px 30px rgba(0,0,0,0.18);
  }
  .card-back {
    background: radial-gradient(ellipse at 40% 40%, #2a2a2a 0%, var(--card-black) 70%);
  }
  .card-front { background: var(--card-white); color: var(--ink); }

  .accent-block {
    position: absolute; top: 30px; right: 0;
    width: 44px; height: 58px; background: var(--ink);
  }
  .person {
    position: absolute; top: 34px; right: 62px; text-align: left;
  }
  .person-name {
    font-family: "Oswald", sans-serif; font-weight: 700;
    font-size: 32px; letter-spacing: 0.5px; line-height: 1; text-transform: uppercase;
  }
  .person-title {
    font-family: "Arimo", sans-serif; font-size: 19px; color: var(--ink-soft);
    margin-top: 6px; margin-left: 88px;
  }
  .rule-long {
    position: absolute; top: 116px; left: 210px; width: 350px; height: 2px; background: var(--rule);
  }
  .brand {
    position: absolute; top: 176px; left: 46px;
    display: flex; align-items: center; gap: 12px;
  }
  .brand-square { width: 18px; height: 18px; background: var(--ink); }
  .brand-name {
    font-family: "Oswald", sans-serif; font-weight: 500;
    font-size: 34px; line-height: 1; text-transform: uppercase; color: var(--ink);
  }
  .rule-short {
    position: absolute; top: 250px; left: 46px; width: 210px; height: 2px; background: var(--rule);
  }
  .contact {
    position: absolute; top: 268px; left: 46px;
    font-family: "Arimo", sans-serif; font-size: 18px; line-height: 1.22; color: var(--ink-soft);
  }
  .address { margin-bottom: 8px; }
  .contact-line { display: flex; align-items: center; gap: 8px; margin-left: 30px; }
  .contact-line svg { width: 15px; height: 15px; flex: none; }
</style>
</head>
<body>
<main class="canvas">
  <section class="card card-back" role="img" aria-label="Card reverse: repeated outline brand pattern on glossy black"></section>

  <section class="card card-front">
    <div class="accent-block"></div>
    <div class="person">
      <div class="person-name">Daniel Arkwright</div>
      <div class="person-title">Executive Director</div>
    </div>
    <div class="rule-long"></div>

    <div class="brand">
      <span class="brand-square"></span>
      <span class="brand-name">Torvane Systems</span>
    </div>
    <div class="rule-short"></div>

    <div class="contact">
      <div class="address">P.O. Box: 48210, Harlow Lane<br>Leeds, United Kingdom</div>
      <div class="contact-line">
        <svg viewBox="0 0 16 16"><path d="M3 1.5l3 .5 1 3-2 1.5a9 9 0 0 0 4.5 4.5L11 9l3 1 .5 3-2 1.5C7 14 2 9 1.5 3.5z" fill="#111"/></svg>
        <span>+44-0113-496-0720</span>
      </div>
      <div class="contact-line">
        <svg viewBox="0 0 16 16"><rect x="1" y="3" width="14" height="10" fill="#111"/><path d="M1.5 3.5L8 9l6.5-5.5" stroke="#fff" stroke-width="1.3" fill="none"/></svg>
        <span>contact@torvanesystems.com</span>
      </div>
      <div class="contact-line">
        <svg viewBox="0 0 16 16"><circle cx="8" cy="8" r="7" fill="#111"/><path d="M1.5 8h13M8 1c-3 3.5-3 10.5 0 14M8 1c3 3.5 3 10.5 0 14" stroke="#fff" stroke-width="1" fill="none"/></svg>
        <span>www.torvanesystems.com</span>
      </div>
    </div>
  </section>
</main>
</body>
</html>
```